Brochure Design - Non-Profit Fundraising Stream

We are a non-profit organization that is developing a fundraising project through the donation of life insurance policies. We have three brochures in each English and French that we developed for a sister organization that we want to reintegrate with our Foundation, keeping the same copy text just changing the logos, colors and make it overall more visually appealing. The foundation is called the 'Marrick-Tolle Syndrome Foundation Canada'.
The original files in .docx format are attached as is the full logo and two symbol files. The deliverables would be six documents in total (InDesign or .docx), each brochure in English and French. The color hex codes are:
red: #7b2850
dark blue: #2c79a7
pale blue: #78b2e2

```html
<!DOCTYPE html>
<html lang="en">
<head>
<meta charset="utf-8">
<title>Marrick-Tolle Syndrome Foundation Canada – Policy Donation FAQ</title>
<link rel="stylesheet" href="https://fonts.googleapis.com/css2?family=Montserrat:wght@400;700&family=Roboto+Condensed:wght@700&display=swap">
<style>
  :root{
    --red:#74244f;
    --navy:#4060ad;
    --dark-blue:#2c79a7;
    --mid-blue:#3089c2;
    --pale-blue:#78b2e2;
    --row-tint:#c2e6f6;
    --ink:#1d1d1f;
    --white:#ffffff;
  }
  *{box-sizing:border-box;margin:0;padding:0}
  html,body{width:849px;height:1200px;overflow:hidden;background:var(--white)}
  .sheet{position:relative;width:849px;height:1200px;overflow:hidden;font-family:"Montserrat",sans-serif;color:var(--ink)}
  .header-band{position:absolute;left:0;top:0;width:849px;height:320px;
    background:linear-gradient(100deg,var(--pale-blue) 0%,var(--mid-blue) 35%,var(--navy) 70%);
    clip-path:polygon(0 0,100% 0,100% 100%,0 72%)}
  .header-rule{position:absolute;left:0;top:0;width:849px;height:340px;
    background:var(--pale-blue);clip-path:polygon(0 67.5%,100% 94%,100% 97%,0 70.5%)}
  .brand{position:absolute;left:396px;top:92px;color:var(--white);display:flex;align-items:center;gap:12px}
  .brand-name{font-size:13px;line-height:1.25}
  .brand-name .main{display:block;font-size:38px;line-height:1.05;letter-spacing:-.5px}
  .brand-dot{width:34px;height:34px;border-radius:50%;background:var(--white)}
  .faq{position:absolute;left:52px;top:358px;width:745px;font-size:12.2px;line-height:12.8px;letter-spacing:-.05px}
  .row{display:grid;grid-template-columns:250px 1fr;border-bottom:1px solid #2a2a2a;background:var(--white)}
  .row:nth-child(odd){background:var(--row-tint)}
  .row.head{background:var(--dark-blue);color:var(--white);font-weight:700;border-bottom:none;letter-spacing:.5px}
  .row>div{padding:0 6px;display:flex;flex-direction:column;justify-content:center}
  .row .a{padding-left:0}
  .a ul{list-style:none}
  .a li{position:relative;padding-left:26px}
  .a li::before{content:"";position:absolute;left:2px;top:5px;width:4px;height:4px;border-radius:50%;background:var(--ink)}
  .footer{position:absolute;left:0;top:1071px;width:815px;height:58px;background:var(--mid-blue);color:var(--white);font-family:"Roboto Condensed",sans-serif;font-weight:700;font-size:30px}
  .footer .tab{position:absolute;left:0;top:0;width:212px;height:58px;background:var(--red);clip-path:polygon(0 0,100% 0,94% 55%,77% 100%,0 100%)}
  .footer span{position:absolute;top:11px;line-height:36px}
  .call{left:82px}
  .phone{left:210px}
  .sep{left:447px;color:var(--red)}
  .mail{left:470px;letter-spacing:-.3px}
</style>
</head>
<body>
<div class="sheet">
  <div class="header-band" role="img" aria-label="Blue gradient header band"></div>
  <div class="header-rule" aria-hidden="true"></div>

  <div class="brand">
    <div class="brand-name">Fondation du syndrome<span class="main">Marrick-Tolle</span>Syndrome Foundation · Canada</div>
    <div class="brand-dot"></div>
  </div>

  <div class="faq">
    <div class="row head" style="height:22px"><div>QUESTIONS</div><div class="a">ANSWERS</div></div>
    <div class="row" style="height:22px"><div>What types of policies are eligible?</div><div class="a">Term/permanent (whole life and universal)</div></div>
    <div class="row" style="height:25px"><div>Who pays for medical underwriting?</div><div class="a">The Foundation</div></div>
    <div class="row" style="height:34px"><div>Who pays for actuarial underwriting?</div><div class="a">The Foundation</div></div>
    <div class="row" style="height:22px"><div>What size policies do you accept?</div><div class="a">Between $50k and $10m</div></div>
    <div class="row" style="height:60px"><div>What are your selection criteria?</div><div class="a">We are working with a life expectancy (LE) calculation of up to 5 years. However, depending upon the circumstances we could go beyond 5 years. Rule of thumb: insured is 70 years old and over, with a medical condition or 80 years old and over, without medical condition.</div></div>
    <div class="row" style="height:35px"><div>Who pays the premiums after the policy has been donated?</div><div class="a">The Foundation</div></div>
    <div class="row" style="height:34px"><div>Who is the beneficiary of the policy after it has been donated?</div><div class="a">The Foundation</div></div>
    <div class="row" style="height:35px"><div>Who is the owner after the policy has been donated?</div><div class="a">The Foundation</div></div>
    <div class="row" style="height:34px"><div>Who does all of the due diligence and underwriting?</div><div class="a">The foundation has partnered with Veldmark Charity Services who looks after these aspects.</div></div>
    <div class="row" style="height:112px"><div>How does the process work?</div><div class="a">You call/email us and give us the following information:
      <ul>
        <li>Face value of the policy</li>
        <li>Annual premium (current and renewal)</li>
        <li>Type of policy</li>
        <li>If term, is it convertible without medical underwriting?</li>
        <li>Policy expiration</li>
        <li>Medical condition(s) of the insured</li>
        <li>Age of the insured</li>
      </ul></div></div>
    <div class="row" style="height:34px"><div>How long does the policy have to have been in force for?</div><div class="a">The policy must be in force for over 2 years.</div></div>
    <div class="row" style="height:86px"><div>How long does the process take?</div><div class="a">Triage: less than a week<br>Medical underwriting: 1-2 weeks<br>Actuarial underwriting: 1 week<br>Actuarial underwriting: 1 week<br>Donation paperwork: 1 day<br>Total time: 3-4 weeks</div></div>
    <div class="row" style="height:34px"><div>What is the typical value of the tax receipt that the donor will receive?</div><div class="a">It varies on the life expectancy calculation, which depends on age and medical situation.</div></div>
    <div class="row" style="height:35px"><div>What if one of my relatives wanted to benefit from the policy?</div><div class="a">Before a policy donation is approved, we must ensure that no relative is interested in taking over the policy.</div></div>
    <div class="row" style="height:22px"><div>Is it legal?</div><div class="a">Yes; the entire process is legal, ethical, and approved by the government.</div></div>
    <div class="row" style="height:47px"><div>But what’s in it for me?</div><div class="a">You had planned to cancel your policy in order to save paying the premiums. The Foundation pays the premiums (you save $$) and you get a tax receipt (good for 5 years) which puts money back into your pocket.</div></div>
  </div>

  <div class="footer">
    <div class="tab"></div>
    <span class="call">Call Us</span>
    <span class="phone">1 (800) 555-0147</span>
    <span class="sep">|</span>
    <span class="mail">donation@veldmark.org</span>
  </div>
</div>
</body>
</html>
```